Retail Jewelry Business Card Design Project

We are in need of a new business card design for a retail jewelry store. This store is in the business of fine jewelry including but not specific to bridal jewelry, diamonds, designer jewelry and watches.

This store has been in business for 20 years but continues to strive for a modern professional appeal. The main colors use for this business are a royal blue, white and silver.

Target Market(s)

Target market is ages 18-50

Industry/Entity Type

Jewelry

Requirements
Must have
• Sales Person Name
Sales Person Email Address

Store Address
Store Phone
Website

Standard business card size. No odd shapes or sizes.
Nice to have
• Overall modern feel for card.

We have thought that a design with a nice feature of the logo on the back of the card would be nice but open to ideas.
Should not have
• No specific images of jewelry should be used.

```html
<!DOCTYPE html>
<html lang="en">
<head>
<meta charset="utf-8">
<title>Marlow Reed Fine Jewelry – Business Card</title>
<link rel="stylesheet" href="https://fonts.googleapis.com/css2?family=Source+Sans+3:wght@400;600&display=swap">
<style>
  :root {
    --page: #ffffff;
    --card-deep: #0b101c;
    --card-mid: #121b31;
    --card-glow: #17264a;
    --monogram: rgba(35, 62, 120, 0.35);
    --white: #ffffff;
    --royal: #3c50b4;
    --icon: #4a60c4;
  }
  * { margin: 0; padding: 0; box-sizing: border-box; }
  html, body { width: 1200px; height: 1000px; overflow: hidden; background: var(--page); }
  body { position: relative; font-family: "Source Sans 3", "Myriad Pro", Arial, sans-serif; color: var(--white); }

  .card {
    position: absolute;
    left: 284px;
    width: 651px;
    overflow: hidden;
    background:
      radial-gradient(ellipse 60% 70% at 48% 58%, var(--card-glow) 0%, var(--card-mid) 45%, var(--card-deep) 100%);
    box-shadow: 3px 4px 7px rgba(0, 0, 0, 0.45);
  }
  .card--front { top: 99px; height: 371px; }
  .card--back { top: 527px; height: 373px; }

  .monogram-area {
    position: absolute;
    top: 0;
    right: 0;
    width: 380px;
    height: 100%;
    background: radial-gradient(ellipse 55% 60% at 55% 45%, var(--monogram) 0%, rgba(35, 62, 120, 0) 75%);
  }

  .brand-name {
    position: absolute;
    font-weight: 400;
    color: var(--white);
    white-space: nowrap;
    letter-spacing: 0.5px;
  }
  .card--front .brand-name { left: 40px; top: 205px; font-size: 38px; }
  .card--back .brand-name { left: 52px; top: 62px; font-size: 40px; }

  .front-web {
    position: absolute;
    left: 74px;
    top: 318px;
    font-size: 16.5px;
    letter-spacing: 1px;
  }

  .person { position: absolute; left: 0; top: 272px; width: 332px; }
  .person__name {
    padding-left: 51px;
    font-size: 20px;
    font-weight: 600;
    color: var(--royal);
    line-height: 1;
  }
  .person__rule { margin-top: 8px; height: 1.5px; background: var(--white); }
  .person__role { padding-left: 51px; margin-top: 6px; font-size: 16px; }

  .contact { position: absolute; left: 350px; top: 222px; font-size: 16px; line-height: 22px; }
  .contact__address { margin-bottom: 4px; }
  .contact__row { display: flex; align-items: center; gap: 9px; }
  .contact__row svg { width: 17px; height: 14px; fill: var(--icon); flex: none; }
</style>
</head>
<body>

<section class="card card--front">
  <div class="monogram-area" role="img" aria-label="Large faint brand monogram decoration"></div>
  <div class="brand-name">Marlow Reed Fine Jewelry</div>
  <div class="front-web">www.marlowreedjewelry.com</div>
</section>

<section class="card card--back">
  <div class="monogram-area" role="img" aria-label="Large faint brand monogram decoration"></div>
  <div class="brand-name">Marlow Reed Fine Jewelry</div>

  <div class="person">
    <div class="person__name">Marlow Reed Halvorsen</div>
    <div class="person__rule"></div>
    <div class="person__role">Owner</div>
  </div>

  <div class="contact">
    <div class="contact__address">2280 Bayview Avenue<br>Port Ellery, FL 32490</div>
    <div class="contact__row">
      <svg viewBox="0 0 17 14" aria-hidden="true"><path d="M1 5 Q8.5 0 16 5 L14 7 L12 5.5 L12 4 Q8.5 3 5 4 L5 5.5 L3 7 Z"/><rect x="4" y="7" width="9" height="6" rx="1"/></svg>
      <span>000.000.0000</span>
    </div>
    <div class="contact__row">
      <svg viewBox="0 0 17 14" aria-hidden="true"><path d="M1 2 H16 V12 H1 Z M2 3 L8.5 8 L15 3 Z" fill-rule="evenodd"/></svg>
      <span>marlow@marlowreedjewelry.com</span>
    </div>
    <div class="contact__row">
      <svg viewBox="0 0 17 14" aria-hidden="true"><circle cx="8.5" cy="7" r="6.3" fill="none" stroke="var(--icon)" stroke-width="1.2"/><ellipse cx="8.5" cy="7" rx="2.8" ry="6.3" fill="none" stroke="var(--icon)" stroke-width="1"/><path d="M2.2 7 H14.8 M3 4 H14 M3 10 H14" stroke="var(--icon)" stroke-width="0.9"/></svg>
      <span>www.marlowreedjewelry.com</span>
    </div>
  </div>
</section>

</body>
</html>
```